Falcrest security business card

Looking for a business card for my security company

Target Market(s)

Security

Industry/Entity Type

Security

Contact Information for Business Card

Name - Gil Marston. Title - General manager - direct 314 862.4490 website www. falcrestsecurityservices.example email - gil@ falcrestsecurityservices.example

Requirements
Must have
• Logo attached

```html
<!DOCTYPE html>
<html lang="en">
<head>
<meta charset="utf-8">
<title>Falcrest Security Services – Business Card</title>
<link rel="stylesheet" href="https://fonts.googleapis.com/css2?family=Saira:wght@500;600;700&display=swap">
<style>
  :root {
    --page-bg: #d9d4cc;
    --card-black: #0c0c0c;
    --card-charcoal: #2c2c2c;
    --gold-light: #e6b978;
    --gold-mid: #c38a45;
    --gold-deep: #8a5524;
    --logo-gold: #d9a85c;
    --ink: #1a1108;
  }
  * { margin: 0; padding: 0; box-sizing: border-box; }
  html, body {
    width: 1200px;
    height: 969px;
    overflow: hidden;
    background: var(--page-bg);
    font-family: "Saira", sans-serif;
  }
  .business-card {
    position: absolute;
    left: 100px;
    top: 200px;
    width: 1000px;
    height: 568px;
    overflow: hidden;
    box-shadow: 0 18px 40px rgba(0,0,0,0.28);
  }
  .card-art {
    position: absolute;
    inset: 0;
    width: 100%;
    height: 100%;
  }
  .brand {
    position: absolute;
    left: 78px;
    top: 170px;
    display: flex;
    align-items: center;
    gap: 14px;
  }
  .brand-dot {
    width: 22px;
    height: 22px;
    border-radius: 50%;
    background: var(--logo-gold);
  }
  .brand-name {
    font-weight: 600;
    font-size: 64px;
    letter-spacing: 2px;
    color: var(--logo-gold);
    line-height: 1;
    text-transform: uppercase;
  }
  .contact {
    position: absolute;
    right: 64px;
    top: 358px;
    text-align: right;
    color: var(--ink);
  }
  .contact-name {
    font-weight: 700;
    font-size: 32px;
    line-height: 1.05;
    letter-spacing: 0.5px;
    text-transform: uppercase;
  }
  .contact-title {
    font-weight: 600;
    font-size: 21px;
    line-height: 1.2;
  }
  .contact-lines {
    margin-top: 26px;
    font-weight: 600;
    font-size: 20px;
    line-height: 1.4;
  }
</style>
</head>
<body>
  <section class="business-card">
    <svg class="card-art" viewBox="0 0 1000 568" preserveAspectRatio="none">
      <defs>
        <linearGradient id="goldField" x1="0" y1="0" x2="1" y2="1">
          <stop offset="0" stop-color="#b7793a"/>
          <stop offset="0.45" stop-color="#d9a55e"/>
          <stop offset="0.75" stop-color="#c08648"/>
          <stop offset="1" stop-color="#8f5a2a"/>
        </linearGradient>
        <radialGradient id="darkField" cx="0.3" cy="0.75" r="0.8">
          <stop offset="0" stop-color="#333333"/>
          <stop offset="1" stop-color="#080808"/>
        </radialGradient>
        <linearGradient id="goldStroke" x1="0" y1="1" x2="1" y2="0">
          <stop offset="0" stop-color="#7a4a1f"/>
          <stop offset="0.5" stop-color="#f0c486"/>
          <stop offset="1" stop-color="#b87d3c"/>
        </linearGradient>
      </defs>
      <rect class="gold-field" width="1000" height="568" fill="url(#goldField)"/>
      <path class="dark-sliver" d="M730 0 H805 C770 250 600 470 300 568 H250 C520 470 700 250 730 0 Z" fill="var(--card-black)"/>
      <path class="dark-field" d="M0 0 H728 C700 250 520 470 230 568 H0 Z" fill="url(#darkField)"/>
      <path class="gold-rule" d="M728 0 C700 250 520 470 230 568" fill="none" stroke="url(#goldStroke)" stroke-width="6"/>
      <path class="gold-swoosh" d="M775 60 C730 300 560 480 330 568" fill="none" stroke="url(#goldStroke)" stroke-width="3"/>
    </svg>

    <div class="brand">
      <span class="brand-dot"></span>
      <span class="brand-name">Falcrest</span>
    </div>

    <div class="contact">
      <p class="contact-name">Gil Marston</p>
      <p class="contact-title">General manager</p>
      <div class="contact-lines">
        <p class="contact-phone">314 862.4490</p>
        <p class="contact-email">gil@ falcrestsecurityservices.example</p>
        <p class="contact-web">falcrestsecurityservices.example</p>
      </div>
    </div>
  </section>
</body>
</html>
```